Staff Assisted Hemodialysis Company Need a fantastic website

Our Company name is: Brellwood Staff Assisted Hemodialysis, we offer a valuable service to renal patients, who cannot dialyze in-center. BSAH sends a licensed nurse to the patient's home, to perform the lifesaving procedure of hemodialysis. Our clinic, which will also perform in-center hemodialysis, offers CKD training as well as a support group where guest speakers, patients, and anyone who wishes to attend can share their experiences. We are the 1st ESRD clinic in Arkansas to offer these services. We would like links to different patient resources (recipes) , as well as a prospective patient interactive form that is HIPAA compliant. We would also like a tab where prospective employees can view our job openings. We would also like to have a map of our location, the qualifications of our staffs, a listing of our affiliations.

Target Market(s)

ESRD patients; people with end stage renal disease, hypertension, or diabetes
people looking to learn about dialysis or kidney failure

Industry/Entity Type

It Company

Number of Pages Required

4 page

Font styles to use
Serif

Colors
a64599
e667a6
f59296
85acd3
85cae6

Requirements
Must have
• Our tagline: " The 1st Staff Assissted Hemodialysis Provider in the State of Arkansas"
• A patient resources tab these can include links to:
• http://www.renalgrid42.example/QTV.php
• http://tulvaralliance.example/
• http://www.hqv.example/Center/Special-Topic/Late-Phase-Nephric-Illness-Center.html
• https://www.nephrahelp.example/
• http://www.cystwell.example/
• We would like a tab listing our Affiliations:
• Delmont Chamber of Commerce
• OLTE - members of
• VBQS- members of

```html
<!DOCTYPE html>
<html lang="en">
<head>
<meta charset="utf-8">
<title>Brellwood Staff Assisted Hemodialysis</title>
<link href="https://fonts.googleapis.com/css2?family=Questrial&display=swap" rel="stylesheet">
<style>
:root{
  --purple:#952f8c;
  --pink:#e0479a;
  --salmon:#f07b87;
  --sky:#6db7df;
  --navy:#1f2f9c;
  --text:#333;
  --muted:#666;
  --line:#e4e4e4;
  --footer:#ececec;
}
*{margin:0;padding:0;box-sizing:border-box}
html,body{width:858px;height:1200px;overflow:hidden;background:#fff}
body{position:relative;font-family:"Questrial",sans-serif;color:var(--text)}
.abs{position:absolute}

.brand{left:69px;top:52px;width:170px;text-align:center;color:var(--navy);line-height:1}
.brand-mark{display:block;width:22px;height:22px;border-radius:50%;background:var(--navy);margin:-40px auto 8px}
.brand-name{font-size:14px;display:block}
.brand-sub{font-size:10px;display:block;margin-top:3px}

.auth{top:20px;height:20px;border-radius:10px;color:#fff;font-size:8px;line-height:20px;text-align:center}
.auth.signup{left:673px;width:54px;background:var(--pink)}
.auth.login{left:733px;width:54px;background:var(--sky)}

.nav{top:65px;left:361px;display:flex;gap:0;font-size:9px}
.nav a{color:#444;text-decoration:none;position:relative}
.nav a.active{color:var(--pink)}
.nav a.active::after{content:"";position:absolute;left:50%;margin-left:-5px;top:25px;border:5px solid transparent;border-bottom-color:var(--pink);border-top:0}

.hero{left:0;top:95px;width:858px;height:380px;background:radial-gradient(ellipse at 55% 45%,#c9876e 0%,#7a5a52 30%,#2f4a4c 65%,#1c3436 100%)}
.tag{left:218px;top:243px;width:422px;height:44px;background:var(--pink);color:#fff;font-size:22px;line-height:44px;text-align:center}
.tag2{left:258px;top:295px;width:340px;height:32px;background:var(--sky);color:#fff;font-size:19px;line-height:32px;text-align:center}
.arrow{top:262px;width:48px;height:48px;border-radius:50%;background:rgba(40,40,40,.55)}
.arrow.prev{left:11px}.arrow.next{left:800px}
.arrow svg{width:48px;height:48px}

.h2{font-size:16px;color:#222;text-align:center;width:858px;left:0}

.card{top:534px;width:170px;height:228px;color:#fff;text-align:center;box-shadow:0 8px 10px -6px rgba(0,0,0,.35)}
.card .photo{height:124px}
.card h3{font-weight:400;font-size:13px;line-height:15px;margin-top:12px;padding:0 14px}
.card p{font-size:8px;line-height:12px;margin-top:7px;padding:0 18px}
.card .more{position:absolute;left:53px;top:190px;width:65px;height:25px;border:1px solid #fff;font-size:8.5px;line-height:23px}
.c1{left:70px;background:var(--purple)} .c1 .photo{background:linear-gradient(135deg,#eef0f2,#b9a49a)}
.c2{left:253px;background:var(--pink)} .c2 .photo{background:linear-gradient(135deg,#f3f5f7,#c4ccd3)}
.c3{left:435px;background:var(--salmon)} .c3 .photo{background:linear-gradient(135deg,#a08a6a,#d9dcdf)}
.c4{left:618px;background:var(--sky)} .c4 .photo{background:linear-gradient(135deg,#2d8a78,#6fb8a4)}

.rule{height:1px;background:var(--line)}
.vrule{width:1px;background:var(--line);top:830px;height:114px}

.col h2{font-weight:400;font-size:16px;color:#222}
.col p{font-size:8.6px;line-height:14px;color:var(--muted)}
.col .lead{font-size:10.5px;color:#333;margin:12px 0 8px}
.col .date{font-size:9px;color:var(--pink);margin-top:8px}

.aff{top:1047px;height:51px;border:1px solid #ededed;font-size:14px;color:#555;display:flex;align-items:center}
.aff b{font-weight:400;color:#aaa;font-size:16px;letter-spacing:.5px;margin-left:4px}
.badge{width:62px;height:62px;border-radius:50%;top:1041px}

.footer{left:0;top:1130px;width:858px;height:70px;background:var(--footer)}
.flinks{left:71px;top:1153px;font-size:8px;color:#444}
.flinks span{margin:0 5px}
.flinks .active{color:var(--pink)}
.copy{left:71px;top:1174px;font-size:8px;color:#777}
.social{top:1155px;width:20px;height:20px;border-radius:50%;background:#c8c8c8}
.social.alt{background:var(--sky)}
</style>
</head>
<body>

<div class="abs brand"><span class="brand-mark"></span><span class="brand-name">Brellwood Staff Assisted</span><span class="brand-sub">Hemodialysis</span></div>

<div class="abs auth signup">SIGN UP</div>
<div class="abs auth login">LOGIN</div>

<nav class="abs nav">
  <a class="active" href="#" style="margin-right:37px">HOME</a>
  <a href="#" style="margin-right:35px">SOLUTIONS</a>
  <a href="#" style="margin-right:37px">SERVICES</a>
  <a href="#" style="margin-right:37px">PROFILES</a>
  <a href="#" style="margin-right:37px">ABOUT</a>
  <a href="#">CONTACT US</a>
</nav>

<div class="abs hero" role="img" aria-label="Photo of gloved clinicians performing a hemodialysis procedure"></div>
<div class="abs tag">The 1st Staff Assissted Hemodialys is</div>
<div class="abs tag2">Provider in the State of Arkansas</div>
<div class="abs arrow prev"><svg viewBox="0 0 48 48"><path d="M28 14 L18 24 L28 34" fill="none" stroke="#fff" stroke-width="3"/></svg></div>
<div class="abs arrow next"><svg viewBox="0 0 48 48"><path d="M20 14 L30 24 L20 34" fill="none" stroke="#fff" stroke-width="3"/></svg></div>

<div class="abs h2" style="top:493px">OUR SERVICES</div>

<div class="abs card c1"><div class="photo" role="img" aria-label="Doctor explaining a kidney model to a patient"></div><h3>Renal Patients</h3><p>Lorem ipsum dolor sit ameonsct etuer adinulorem ipsumm</p><div class="more">Read more</div></div>
<div class="abs card c2"><div class="photo" role="img" aria-label="Clinician preparing a syringe"></div><h3>Who cannot Dialyze in-center</h3><p>Lorem ipsum dolor sit ameonsct</p><div class="more">Read more</div></div>
<div class="abs card c3"><div class="photo" role="img" aria-label="Nurse caring for a patient at home"></div><h3>BSAH sends a licensed Nurse to the Patient's Home</h3><div class="more">Read more</div></div>
<div class="abs card c4"><div class="photo" role="img" aria-label="Surgical team performing a procedure"></div><h3>To Perform the Lifesaving Procedure of Hemodialysis</h3><div class="more">Read more</div></div>

<div class="abs rule" style="left:70px;top:791px;width:718px"></div>

<div class="abs col" style="left:70px;top:820px;width:200px">
  <h2>WHO WE ARE.</h2>
  <p style="margin-top:10px">But I must explain to you how all thismilorsta ken idea of denouncing pleasuitseelf.</p>
  <h2 style="margin-top:16px">WHAT WE DO.</h2>
  <p style="margin-top:10px">But I must explain to you how all thismilorsta ken idea of denouncing pleasuitseelf.</p>
</div>
<div class="abs vrule" style="left:286px"></div>
<div class="abs col" style="left:320px;top:820px;width:215px">
  <h2>LATEST NEWS</h2>
  <p class="lead">Lorem ipsummust explain to you how all</p>
  <p><span style="font-size:10px;color:#555">Adea of denouncing pleasure and praising pain</span><br>was born and I will give you a complete account of the system, and expound the actual.</p>
  <p class="date">April 13 2015</p>
</div>
<div class="abs vrule" style="left:561px"></div>
<div class="abs col" style="left:590px;top:820px;width:200px">
  <h2>ABOUT OUR COMPANY</h2>
  <p style="margin-top:10px;line-height:15.4px">But I must explain to you how all this mistaken idea of denouncing pleasure and praising pain was born and I will give you a complete ac-count of the system, and expound the actual teachings of the great explorer of the truth, the master-builder of human happiness.</p>
</div>

<div class="abs rule" style="left:70px;top:974px;width:718px"></div>
<div class="abs h2" style="top:1006px">OUR AFFILIATIONS</div>

<div class="abs aff" style="left:120px;width:184px;padding-left:41px;line-height:16px">Delmont Chamber<br>of Commerce</div>
<div class="abs badge" style="left:89px;background:var(--pink)"></div>
<div class="abs aff" style="left:352px;width:184px;padding-left:45px">Member of <b>OLTE</b></div>
<div class="abs badge" style="left:321px;background:var(--salmon)"></div>
<div class="abs aff" style="left:584px;width:185px;padding-left:45px">Member of <b>VBQS</b></div>
<div class="abs badge" style="left:553px;background:var(--sky)"></div>

<footer class="abs footer"></footer>
<div class="abs flinks"><span class="active" style="margin-left:0">HOME</span>|<span>SOLUTIONS</span>|<span>SERVICES</span>|<span>PROFILES</span>|<span>ABOUT</span>|<span>CONTACT US</span></div>
<div class="abs copy">Copyright 2015 all rights are reserved</div>
<div class="abs social" style="left:694px"></div>
<div class="abs social alt" style="left:718px"></div>
<div class="abs social" style="left:742px"></div>
<div class="abs social" style="left:767px"></div>

</body>
</html>
```